New bag packaging for chewy candy

We need a new packaging for our fruit chewy candy range (7 flavours in all). The product will have to showcase our trademark and feature the fruit of the product's flavour. We require the packaging to have an equal look and adaptable to 7 flavours, to make it have the appearance that it is part of a range of products as opposed to a standalone. New design preferred. Please keep it playful but simple and yet stand out on an aisle shelf already full of colours. Dimensions of bag is 130mm (W) x 205mm (H). Allow for information on the back folds. Example of existing packaging given. Winner will get extra to adapt the packaging to the other 6 flavours.

Target Market(s)

Supermarket crowd

Industry/Entity Type

Product

Requirements
Must have
• Trademark, Flavour, picture of fruit lfavour
Nice to have
• Open to bold colours

```html
<!DOCTYPE html>
<html lang="en">
<head>
<meta charset="utf-8">
<title>Chompy Bites – Strawberry Chewy Candy</title>
<link rel="stylesheet" href="https://fonts.googleapis.com/css2?family=Great+Vibes&family=Montserrat:wght@500;700;800&display=swap">
<style>
  :root {
    --berry-red: #c8243a;
    --band-red: #b81e30;
    --deep-red: #8e1a2a;
    --ring-red: #a11c2e;
    --white: #ffffff;
    --mist: #d9d9d9;
    --cream: #fbeccb;
    --sun-yellow: #f7c531;
    --candy-pink: #ee6fa0;
    --badge-text: #b8202f;
  }
  html, body {
    margin: 0;
    padding: 0;
    width: 761px;
    height: 1200px;
    overflow: hidden;
    background: var(--white);
  }
  .pack {
    display: block;
    width: 761px;
    height: 1200px;
  }
  .brand-name {
    font-family: "Montserrat", sans-serif;
    font-weight: 800;
    font-size: 54px;
    fill: var(--berry-red);
  }
  .flavour-name {
    font-family: "Great Vibes", cursive;
    font-size: 190px;
    fill: var(--white);
  }
  .product-type {
    font-family: "Great Vibes", cursive;
    font-size: 58px;
    fill: var(--deep-red);
  }
  .badge-label {
    font-family: "Montserrat", sans-serif;
    font-weight: 500;
    font-size: 24px;
    fill: var(--badge-text);
  }
  .badge-vitamin {
    font-family: "Montserrat", sans-serif;
    font-weight: 800;
    font-size: 58px;
    fill: var(--badge-text);
  }
  .badge-detail {
    font-family: "Montserrat", sans-serif;
    font-weight: 700;
    font-size: 28px;
    fill: var(--badge-text);
  }
  .tagline {
    font-family: "Montserrat", sans-serif;
    font-weight: 700;
    font-size: 36px;
    letter-spacing: 1px;
    fill: var(--white);
  }
</style>
</head>
<body>
<svg class="pack" viewBox="0 0 761 1200" xmlns="http://www.w3.org/2000/svg">
  <defs>
    <linearGradient id="header-mist" x1="0" y1="0" x2="0" y2="1">
      <stop offset="0" stop-color="var(--white)"/>
      <stop offset="1" stop-color="var(--mist)"/>
    </linearGradient>
    <linearGradient id="body-red" x1="0" y1="0" x2="1" y2="1">
      <stop offset="0" stop-color="#d02a42"/>
      <stop offset="1" stop-color="#c01f35"/>
    </linearGradient>
    <radialGradient id="fruit-tones" cx="0.55" cy="0.45" r="0.6">
      <stop offset="0" stop-color="#e0394a"/>
      <stop offset="0.6" stop-color="#c9283a"/>
      <stop offset="1" stop-color="#f2f0f0"/>
    </radialGradient>
    <clipPath id="above-footer">
      <rect x="0" y="0" width="761" height="1088"/>
    </clipPath>
    <filter id="soft-shadow" x="-10%" y="-10%" width="120%" height="130%">
      <feDropShadow dx="2" dy="4" stdDeviation="3" flood-color="#5a0c17" flood-opacity="0.45"/>
    </filter>
  </defs>

  <!-- body -->
  <rect class="body-field" x="0" y="0" width="761" height="1200" fill="url(#body-red)"/>

  <!-- header -->
  <path class="header-wave" d="M0 92 H761 V200 C660 290 520 325 380 322 C240 320 110 240 0 160 Z" fill="url(#header-mist)"/>
  <rect class="top-band" x="0" y="0" width="761" height="92" fill="var(--band-red)"/>
  <g class="brand">
    <text class="brand-name" x="380" y="212" text-anchor="middle">Chompy Bites</text>
  </g>

  <!-- flavour ribbon -->
  <g class="ribbon">
    <path class="ribbon-pink" d="M318 612 C430 505 600 450 761 438 V460 C600 470 450 520 330 612 Z" fill="var(--candy-pink)"/>
    <path class="ribbon-cream" d="M290 640 C410 530 590 468 761 458 V590 C580 575 420 590 290 650 Z" fill="var(--cream)"/>
    <path class="ribbon-yellow" d="M248 672 C380 600 560 572 761 588 V622 C560 605 380 622 256 676 Z" fill="var(--sun-yellow)"/>
  </g>

  <!-- flavour title -->
  <text class="flavour-name" x="36" y="560" textLength="690" lengthAdjust="spacingAndGlyphs" transform="rotate(-9 36 560)" filter="url(#soft-shadow)">Strawberry</text>
  <text class="product-type" x="400" y="570" transform="rotate(-13 400 570)">Chewy Candy</text>

  <!-- fruit showcase -->
  <g clip-path="url(#above-footer)">
    <circle class="showcase-ring" cx="512" cy="1080" r="446" fill="var(--ring-red)" opacity="0.55"/>
    <circle class="showcase-dome" cx="512" cy="1080" r="420" fill="var(--white)"/>
    <g role="img" aria-label="Photo of whole and halved strawberries with pink chewy candies">
      <ellipse cx="500" cy="935" rx="260" ry="150" fill="url(#fruit-tones)"/>
    </g>
  </g>

  <!-- footer -->
  <rect class="footer-band" x="0" y="1088" width="761" height="112" fill="var(--band-red)"/>
  <rect class="footer-rule" x="270" y="1086" width="491" height="3" fill="var(--white)"/>
  <text class="tagline" x="712" y="1147" text-anchor="end">UNIQUE TASTE</text>

  <!-- ingredient badge -->
  <g class="badge">
    <circle cx="120" cy="1040" r="150" fill="var(--white)" stroke="var(--ring-red)" stroke-width="10"/>
    <text class="badge-label" x="126" y="950" text-anchor="middle">Contains:</text>
    <text class="badge-vitamin" x="124" y="1015" text-anchor="middle">VIT–C</text>
    <text class="badge-detail" x="124" y="1054" text-anchor="middle">+</text>
    <text class="badge-detail" x="126" y="1090" text-anchor="middle">Conc.</text>
    <text class="badge-detail" x="126" y="1124" text-anchor="middle">Apple Juice</text>
  </g>
</svg>
</body>
</html>
```